Stationery Design for Pfotenhaus

We already have a logo a Logo for our outstanding veterinary hospital. Now we are looking for our future letterhead, business cards and envelopes. We would like to see a design using the color from our logo. Additional color should be limited to grey or a rusty brown. The font should be easy and clearly readable and must be easily available on all computers (to install it in our Management software). The finial design should communicate competence in veterinary medicine, and empathy.

To meet the European regulation (DIN5008) there are a couple mandatory legal informations one the letterhead. We also enclosed a template of exact measurement, which need to be respected according to DIN5008.

Mandatory legal information are (best placed in the footer):
"Pfotenhaus GmbH & Co KG, Brunnfeldgasse 417C, 1140 Wien,
Handelsgericht Wien, FN 294617k, GF: Dr. Lorenz Haidinger
ATU 3918462"
Additional informations needed:
"Tel: +43 1 5849162, Fax: +43 1 5849163, info@pfotenhaus-demo.at, www. pfotenhaus-demo.at"
bank account informations should be included as well. These are:
"Sparkasse Hollental Nord, IBAN: AT 58 1111 2222 3333 4444, BIC: HLNTAT2H517"

The Logo should be in the upper right corner. Below that we need a space for informations regarding the responsible veterinarians. There will be 3-5 Names, each of it consisting of 2 lines (see example below). The Names should be highlighted (larger font) compared to the qualifications in the second line.
Tierärztliche Leitung:
Dr. Lorenz Haidinger
Diplomate ECVS
Updates

The contest was startet on the 2nd of may and the deadline was a day later? Why was that so fast? Did I do something wrong? BR

Target Market(s)

dog and cat owner in Austria as welle as referring veterinarians in Austria

Industry/Entity Type

Veterinary

Contact Information for Business Card

One side: Logo
other side:
Dr. Lorenz Haidinger
Diplomate ECVS
EBVS Specialist of Small Animal Surgery

Pfotenhaus GmbH&Co KG
Brunnfeldgasse 417C
1140 Wien

Tel: +43 1 5849160 DW 102
Fax: +43 1 5849160 DW 999
email: lorenz.haidinger@pfotenhaus-demo.at

Font styles to use
Serif
Sans Serif

Requirements
Must have
• The logo should be given in the upper right. Most of the legal informations should be given in the footer. The upper left Area should be clear, since the recipient address will be placed there.
Colors should be limited to golden, blue and greyscale (two different gereysacales at most).

```html
<!DOCTYPE html>
<html lang="de">
<head>
<meta charset="utf-8">
<title>Pfotenhaus – Geschäftsausstattung</title>
<link href="https://fonts.googleapis.com/css2?family=Roboto:wght@400;500;700&display=swap" rel="stylesheet">
<style>
  :root{
    --navy:#1b2a57;
    --gold:#d9a62a;
    --ink:#2b2b2b;
    --bg:#e4e5e8;
    --paper:#ffffff;
    --wm-gold:#f6efe1;
  }
  *{box-sizing:border-box;margin:0;padding:0}
  html,body{width:1200px;height:1200px;overflow:hidden}
  body{background:var(--bg);font-family:"Roboto",Arial,sans-serif;position:relative;color:var(--ink)}

  /* ---------- letterhead ---------- */
  .letterhead{position:absolute;left:420px;top:62px;width:760px;height:1075px;background:var(--paper);box-shadow:0 2px 8px rgba(0,0,0,.12)}
  .brand{position:absolute;display:flex;align-items:center}
  .brand-dot{border-radius:50%;border:3px solid var(--gold);background:var(--navy);flex:none}
  .brand-name{font-weight:700;color:var(--navy);letter-spacing:-.5px}
  .letterhead .brand{left:84px;top:46px}
  .letterhead .brand-dot{width:78px;height:78px}
  .letterhead .brand-name{font-size:30px;margin-left:14px}

  .vets{position:absolute;left:84px;top:156px;width:400px}
  .vets-title{font-size:13px;color:var(--ink);margin-bottom:10px}
  .vets-grid{display:grid;grid-template-columns:178px 200px;row-gap:11px}
  .vet-name{font-size:13px;font-weight:500;color:var(--navy);line-height:14px}
  .vet-role{font-size:12.5px;color:var(--gold);line-height:14px}

  .watermark{position:absolute;left:234px;top:446px;width:296px;height:296px}

  .lh-footer{position:absolute;left:84px;right:0;top:943px}
  .footer-head{display:flex;align-items:center}
  .company{font-size:15.5px;font-weight:500;color:var(--navy);white-space:nowrap}
  .rule{flex:1;margin-left:14px;height:6px;border-top:2.5px solid var(--navy);border-bottom:2.5px solid var(--gold)}
  .footer-cols{display:flex;margin-top:12px;font-size:11px;line-height:14px;color:var(--ink)}
  .col-legal{width:200px;padding-right:10px}
  .col-contact{width:190px;border-left:1.5px solid var(--gold);border-right:1.5px solid var(--gold);padding-left:28px;height:60px}
  .col-bank{padding-left:36px;padding-top:2px}
  .contact-row{display:flex;align-items:center;gap:10px;height:15px}
  .icon{width:11px;height:11px;flex:none}

  /* ---------- business cards ---------- */
  .card{position:absolute;left:25px;width:456px;height:284px;background:var(--paper);border-radius:8px;box-shadow:0 2px 8px rgba(0,0,0,.15);transform:scale(.8);transform-origin:0 0;overflow:hidden}
  .card-front{top:300px}
  .card-back{top:560px}
  .card-front .brand{left:0;right:0;top:0;bottom:0;flex-direction:column;justify-content:center}
  .card-front .brand-dot{width:115px;height:115px}
  .card-front .brand-name{font-size:40px;margin-top:16px}

  .card-back .brand{left:29px;top:16px}
  .card-back .brand-dot{width:115px;height:115px}
  .person{position:absolute;right:20px;top:26px;text-align:right}
  .person-name{font-size:25px;font-weight:700;color:var(--gold);line-height:30px}
  .person-title{font-size:15.5px;color:var(--navy);margin-top:6px}
  .person-spec{font-size:14px;color:var(--navy);margin-top:6px}
  .card-company{position:absolute;left:27px;right:0;top:154px;display:flex;align-items:center}
  .card-company .company{font-size:19px}
  .card-contact{position:absolute;left:27px;top:187px;font-size:14px;color:var(--ink)}
  .card-contact .contact-row{height:20px;gap:12px}
  .card-contact .icon{width:13px;height:13px}
</style>
</head>
<body>

<section class="letterhead">
  <div class="brand">
    <span class="brand-dot"></span>
    <span class="brand-name">Pfotenhaus</span>
  </div>

  <div class="vets">
    <p class="vets-title">Tierärztliche Leitung</p>
    <div class="vets-grid">
      <div><p class="vet-name">Dr. Lorenz Haidinger</p><p class="vet-role">Diplomate ECVS</p></div>
      <div><p class="vet-name">Names of veterinarians</p><p class="vet-role">function in yellow</p></div>
      <div><p class="vet-name">Names of veterinarians</p><p class="vet-role">function in yellow</p></div>
      <div><p class="vet-name">Names of veterinarians</p><p class="vet-role">function in yellow</p></div>
      <div><p class="vet-name">Names of veterinarians</p><p class="vet-role">function in yellow</p></div>
    </div>
  </div>

  <svg class="watermark" viewBox="0 0 296 296" role="img" aria-label="Faint brand circle decoration">
    <circle cx="148" cy="148" r="143" fill="none" stroke="var(--wm-gold)" stroke-width="7"/>
  </svg>

  <footer class="lh-footer">
    <div class="footer-head">
      <span class="company">Pfotenhaus GmbH &amp; Co KG</span>
      <span class="rule"></span>
    </div>
    <div class="footer-cols">
      <div class="col-legal">
        Brunnfeldgasse 417C, 1140 Wien,<br>
        Handelsgericht Wien, FN 294617k,<br>
        GF: Dr. Lorenz Haidinger<br>
        ATU 3918462
      </div>
      <div class="col-contact">
        <div class="contact-row"><svg class="icon" viewBox="0 0 12 12"><path d="M2 1l2 0 1 3-1.5 1a6 6 0 0 0 3.5 3.5L8 7l3 1v2a1 1 0 0 1-1 1A9 9 0 0 1 1 2a1 1 0 0 1 1-1z" fill="var(--gold)"/></svg>+43 1 5849162</div>
        <div class="contact-row"><svg class="icon" viewBox="0 0 12 12"><rect x="3" y="1" width="6" height="3" fill="var(--gold)"/><rect x="1" y="4.5" width="10" height="5" rx="1" fill="var(--gold)"/><rect x="3" y="8" width="6" height="3" fill="var(--gold)"/></svg>+43 1 5849163</div>
        <div class="contact-row"><svg class="icon" viewBox="0 0 12 12"><rect x="1" y="2.5" width="10" height="7" fill="var(--gold)"/><path d="M1 2.5l5 4 5-4" fill="none" stroke="#fff" stroke-width="1"/></svg>info@pfotenhaus-demo.at</div>
        <div class="contact-row"><svg class="icon" viewBox="0 0 12 12"><circle cx="6" cy="6" r="5" fill="var(--gold)"/><path d="M1 6h10M6 1v10M6 1c-3 3-3 7 0 10M6 1c3 3 3 7 0 10" fill="none" stroke="#fff" stroke-width=".7"/></svg>www.pfotenhaus-demo.at</div>
      </div>
      <div class="col-bank">
        Sparkasse Hollental Nord,<br>
        IBAN: AT 58 1111 2222 3333 4444,<br>
        BIC: HLNTAT2H517
      </div>
    </div>
  </footer>
</section>

<section class="card card-front">
  <div class="brand">
    <span class="brand-dot"></span>
    <span class="brand-name">Pfotenhaus</span>
  </div>
</section>

<section class="card card-back">
  <div class="brand"><span class="brand-dot"></span></div>
  <div class="person">
    <p class="person-name">Dr. Lorenz Haidinger</p>
    <p class="person-title">Diplomate ECVS</p>
    <p class="person-spec">EBVS Specialist of Small Animal Surgery</p>
  </div>
  <div class="card-company">
    <span class="company">Pfotenhaus GmbH&amp;Co KG</span>
    <span class="rule"></span>
  </div>
  <div class="card-contact">
    <div class="contact-row"><svg class="icon" viewBox="0 0 12 12"><path d="M6 11C3 7 2 5.5 2 4a4 4 0 0 1 8 0c0 1.5-1 3-4 7z" fill="var(--gold)"/><circle cx="6" cy="4" r="1.4" fill="#fff"/></svg>Brunnfeldgasse 417C 1140 Wien</div>
    <div class="contact-row"><svg class="icon" viewBox="0 0 12 12"><path d="M2 1l2 0 1 3-1.5 1a6 6 0 0 0 3.5 3.5L8 7l3 1v2a1 1 0 0 1-1 1A9 9 0 0 1 1 2a1 1 0 0 1 1-1z" fill="var(--gold)"/></svg>+43 1 5849160 DW 102</div>
    <div class="contact-row"><svg class="icon" viewBox="0 0 12 12"><rect x="3" y="1" width="6" height="3" fill="var(--gold)"/><rect x="1" y="4.5" width="10" height="5" rx="1" fill="var(--gold)"/><rect x="3" y="8" width="6" height="3" fill="var(--gold)"/></svg>+43 1 5849160 DW 999</div>
    <div class="contact-row"><svg class="icon" viewBox="0 0 12 12"><circle cx="6" cy="6" r="5" fill="var(--gold)"/><path d="M1 6h10M6 1v10M6 1c-3 3-3 7 0 10M6 1c3 3 3 7 0 10" fill="none" stroke="#fff" stroke-width=".7"/></svg>lorenz.haidinger@pfotenhaus-demo.at</div>
  </div>
</section>

</body>
</html>
```